Pickwick Lake Billboard

Looking to design a multi purpose billboard promoting Pickwick Lake as a destination point. Billboard size is 12ft x 40ft
My goal is to advertise our restaurant The Driftwood (pic attached)
What makes Pickwick a destination? It offers lodging / water skiing / Off Road Adventure / Camping / Fishing / Hunting
Want a catch phrase, something like "Looking For a Getaway" or "Need a Break"
Needs to really pop and catch the interest of the looker
maybe have our website address www.marbrydriftwood.com
Open for ideas

Need extra days to review

```html
<!DOCTYPE html>
<html lang="en">
<head>
<meta charset="utf-8">
<title>The Driftwood – Pickwick Lake Billboard</title>
<link rel="stylesheet" href="https://fonts.googleapis.com/css2?family=Playfair+Display:wght@700;900&family=Playfair+Display+SC:wght@700;900&display=swap">
<style>
  :root {
    --page-bg: #e6e6e4;
    --board-dark: #121111;
    --board-warm: #231a16;
    --ink-white: #ffffff;
    --accent-yellow: #f6b800;
    --tile-orange: #d68d1e;
    --tile-border: #f1e6d4;
    --tile-art: #e7a948;
    --tape: rgba(201, 154, 88, 0.85);
    --photo-frame: #f7f7f5;
    --photo-store: #7a4a22;
    --photo-store-glow: #c7762c;
    --photo-sky: #6f7fb0;
    --photo-sunset: #e98a72;
    --photo-water: #3b4b78;
  }
  * { box-sizing: border-box; margin: 0; padding: 0; }
  html, body {
    width: 1200px; height: 962px; overflow: hidden;
    background: var(--page-bg);
  }
  .billboard {
    position: absolute; left: 0; top: 328px;
    width: 1200px; height: 305px; overflow: hidden;
    background: linear-gradient(90deg, var(--board-dark) 0%, #1a1716 55%, var(--board-warm) 100%);
    font-family: "Playfair Display", Georgia, serif;
    color: var(--ink-white);
  }
  .snapshot {
    position: absolute;
    background: var(--photo-frame);
    padding: 6px;
    box-shadow: 0 4px 10px rgba(0,0,0,0.55);
  }
  .snapshot .photo { width: 100%; height: 100%; }
  .snapshot--store { left: 128px; top: 34px; width: 250px; height: 180px; transform: rotate(-7deg); }
  .snapshot--store .photo {
    background: linear-gradient(160deg, #3d5a34 0%, var(--photo-store) 35%, var(--photo-store-glow) 70%, #5a3a20 100%);
  }
  .snapshot--sunset { left: 266px; top: 150px; width: 176px; height: 128px; transform: rotate(-8deg); }
  .snapshot--sunset .photo {
    background: linear-gradient(180deg, var(--photo-sky) 0%, #a98aa6 38%, var(--photo-sunset) 50%, var(--photo-water) 62%, #1f2a4a 100%);
  }
  .tape { position: absolute; width: 56px; height: 14px; background: var(--tape); }
  .tape--top-left { left: 104px; top: 52px; transform: rotate(-52deg); }
  .tape--middle { left: 254px; top: 166px; transform: rotate(-50deg); }
  .tape--bottom-right { left: 406px; top: 262px; transform: rotate(-50deg); }

  .brand { position: absolute; left: 462px; top: 0; width: 272px; text-align: center; white-space: nowrap; }
  .brand__the {
    position: absolute; top: 32px; left: 0; width: 100%;
    font-family: "Playfair Display SC", Georgia, serif; font-weight: 700;
    font-size: 22px; line-height: 1;
  }
  .brand__name {
    position: absolute; top: 66px; left: 0; width: 100%;
    font-family: "Playfair Display SC", Georgia, serif; font-weight: 900;
    font-size: 38px; line-height: 1;
  }
  .brand__place {
    position: absolute; top: 118px; left: 0; width: 100%;
    font-family: "Playfair Display SC", Georgia, serif; font-weight: 700;
    font-size: 18px; line-height: 1;
  }
  .tagline {
    position: absolute; left: 458px; top: 164px; width: 280px;
    text-align: center; font-weight: 900; font-size: 41px; line-height: 46px;
    white-space: nowrap;
  }
  .tagline__highlight { color: var(--accent-yellow); }
  .arrow { position: absolute; left: 0; top: 0; width: 1200px; height: 305px; pointer-events: none; }

  .offers__title {
    position: absolute; left: 775px; top: 30px;
    font-weight: 900; font-size: 25px; line-height: 1; white-space: nowrap;
  }
  .offer {
    position: absolute; width: 91px; height: 95px;
    background: var(--tile-orange);
    border: 2px solid var(--tile-border);
    text-align: center;
  }
  .offer__art {
    position: absolute; left: 18px; top: 12px; width: 51px; height: 48px;
    background: var(--tile-art); border-radius: 3px;
  }
  .offer__label {
    position: absolute; left: 0; right: 0; bottom: 11px;
    font-weight: 700; font-size: 11px; line-height: 1.0; color: var(--ink-white);
    white-space: nowrap;
  }
  .offer__label--two-line { bottom: 6px; }
  .col-1 { left: 777px; } .col-2 { left: 879px; } .col-3 { left: 981px; }
  .row-1 { top: 76px; } .row-2 { top: 181px; }
</style>
</head>
<body>
  <section class="billboard" aria-label="The Driftwood Pickwick Lake billboard">
    <figure class="snapshot snapshot--store">
      <div class="photo" role="img" aria-label="Photo of The Driftwood rustic wooden storefront lit at dusk"></div>
    </figure>
    <figure class="snapshot snapshot--sunset">
      <div class="photo" role="img" aria-label="Photo of a sunset over Pickwick Lake"></div>
    </figure>
    <span class="tape tape--top-left"></span>
    <span class="tape tape--middle"></span>
    <span class="tape tape--bottom-right"></span>

    <svg class="arrow" viewBox="0 0 1200 305" aria-hidden="true">
      <g fill="none" stroke="#ffffff" stroke-width="1.4" stroke-linecap="round">
        <path d="M459 74 C428 72 400 86 390 110"/>
        <path d="M385 102 L390 110 L397 103"/>
        <path d="M682 272 C720 280 748 266 756 238"/>
        <path d="M750 243 L756 237 L759 246"/>
      </g>
    </svg>

    <header class="brand">
      <div class="brand__the">THE</div>
      <h1 class="brand__name">DRIFTWOOD</h1>
      <div class="brand__place">PICKWICK LAKE &amp; DAM</div>
    </header>

    <h2 class="tagline">Looking For<br>a <span class="tagline__highlight">Getaway?</span></h2>

    <h3 class="offers__title">Pickwick Offers:</h3>
    <div class="offer col-1 row-1"><div class="offer__art" role="img" aria-label="Cabin among pine trees icon"></div><span class="offer__label">Lodging</span></div>
    <div class="offer col-2 row-1"><div class="offer__art" role="img" aria-label="Mountain peaks icon"></div><span class="offer__label">Camping</span></div>
    <div class="offer col-3 row-1"><div class="offer__art" role="img" aria-label="Leaping fish icon"></div><span class="offer__label">Fishing</span></div>
    <div class="offer col-1 row-2"><div class="offer__art" role="img" aria-label="Deer antlers icon"></div><span class="offer__label">Hunting</span></div>
    <div class="offer col-2 row-2"><div class="offer__art" role="img" aria-label="Water skier icon"></div><span class="offer__label">Water Skiing</span></div>
    <div class="offer col-3 row-2"><div class="offer__art" role="img" aria-label="Off road vehicle and mountains icon"></div><span class="offer__label offer__label--two-line">Off Road<br>Adventure</span></div>
  </section>
</body>
</html>
```